Design a compelling Varnelo Business Card that will drive people to my site

I want a business card that I can give to people—less to tell them who I am and more to direct them to my website. My website is a portal for Tidewell Aquatics Officials and a place for people who want to become Tidewell Aquatics Officials.
I am uploading my official company logo as well as a business card mockup that I did on my own. Please feel free to completely stray from this design.
I've included a screen recording of the homepage of my website as well.
Target Market(s)
Tidewell Aquatics Officials and people who desire to become one
Contact Information for Business Card
website url
Look and feel
Each slider illustrates characteristics of the customer's brand and the style your logo design should communicate.

```html
<!DOCTYPE html>
<html lang="en">
<head>
<meta charset="utf-8">
<title>Varnelo Business Card</title>
<link rel="stylesheet" href="https://fonts.googleapis.com/css2?family=Montserrat:wght@400;500;700&display=swap">
<style>
  :root {
    --navy: #3a53a6;
    --navy-deep: #2f4696;
    --periwinkle: #97a9d7;
    --white: #ffffff;
    --stage: #e4e5e8;
  }
  * { margin: 0; padding: 0; box-sizing: border-box; }
  html, body { width: 1200px; height: 915px; overflow: hidden; }
  body {
    background: var(--stage);
    font-family: "Montserrat", sans-serif;
    position: relative;
  }
  .card {
    position: absolute;
    left: 290px;
    width: 620px;
    height: 354px;
    border-radius: 18px;
    overflow: hidden;
    box-shadow: 0 6px 18px rgba(0,0,0,0.18);
  }
  .card-front {
    top: 80px;
    background: radial-gradient(circle at 70% 25%, #4a63b2 0%, var(--navy) 55%, var(--navy-deep) 100%);
    display: flex;
    align-items: center;
    justify-content: center;
  }
  .card-back { top: 481px; background: var(--white); }

  .wordmark {
    display: flex;
    align-items: center;
    gap: 12px;
    font-weight: 700;
    letter-spacing: -1px;
    line-height: 1;
  }
  .wordmark-dot { border-radius: 50%; flex: none; }
  .card-front .wordmark { font-size: 74px; color: var(--white); }
  .card-front .wordmark-dot { width: 22px; height: 22px; background: var(--periwinkle); }

  .card-back .wordmark {
    position: absolute;
    top: 58px;
    left: 0;
    right: 0;
    justify-content: center;
    font-size: 60px;
    color: var(--navy);
  }
  .card-back .wordmark-dot { width: 18px; height: 18px; background: var(--periwinkle); }

  .band-name {
    position: absolute;
    left: 0;
    top: 196px;
    width: 362px;
    height: 118px;
    background: var(--periwinkle);
    color: var(--white);
    text-align: right;
    padding: 28px 22px 0 0;
  }
  .person-name { font-weight: 700; font-size: 24px; }
  .person-role { font-weight: 400; font-size: 16px; margin-top: 4px; }

  .band-contact {
    position: absolute;
    left: 374px;
    top: 148px;
    right: 0;
    height: 124px;
    background: var(--navy);
    color: var(--white);
    padding: 20px 0 0 20px;
    display: flex;
    flex-direction: column;
    gap: 12px;
    font-size: 15px;
    font-weight: 500;
  }
  .contact-line { display: flex; align-items: center; gap: 10px; }
  .contact-line svg { width: 15px; height: 15px; flex: none; }
</style>
</head>
<body>
  <section class="card card-front" role="img" aria-label="Varnelo card front: deep blue field with soft water bubbles and the brand name">
    <div class="wordmark"><span class="wordmark-dot"></span><span>varnelo</span></div>
  </section>

  <section class="card card-back">
    <div class="wordmark"><span class="wordmark-dot"></span><span>varnelo</span></div>

    <div class="band-name">
      <div class="person-name">Martin Ashby</div>
      <div class="person-role">CEO &amp; Founder</div>
    </div>

    <div class="band-contact">
      <div class="contact-line">
        <svg viewBox="0 0 16 16" fill="none" stroke="#fff" stroke-width="1.5"><path d="M3 2h3l1.5 3.5-2 1.2a8 8 0 0 0 3.8 3.8l1.2-2L14 10v3a1.5 1.5 0 0 1-1.5 1.5A11 11 0 0 1 1.5 3.5 1.5 1.5 0 0 1 3 2z"/></svg>
        <span>(555) 271-0438</span>
      </div>
      <div class="contact-line">
        <svg viewBox="0 0 16 16" fill="none" stroke="#fff" stroke-width="1.5"><rect x="1.5" y="3.5" width="13" height="9" rx="1"/><path d="M2 4l6 5 6-5"/></svg>
        <span>martin@varnelo.com</span>
      </div>
      <div class="contact-line">
        <svg viewBox="0 0 16 16" fill="none" stroke="#fff" stroke-width="1.3"><circle cx="8" cy="8" r="6.5"/><ellipse cx="8" cy="8" rx="3" ry="6.5"/><path d="M1.5 8h13M2.5 5h11M2.5 11h11"/></svg>
        <span>www.varnelo.com</span>
      </div>
    </div>
  </section>
</body>
</html>
```